Healthcare website - Diabetic Shoes - Vitacor - No Cost

I am looking to upgrade my website. I do not want to use Wordpress, Adobe Muse or another designing program. The code should be easily editable using textpad or VI. After the project is done I want to easily add my custom PHP code.

Features
Creative and Modern Design .
Fully responsive site for use on mobile devices
bootstrap, jquery

My current website is
www.stridewellfeet.com

Target Market(s)

Older people who have diabetes. Target market is +60 years old, but we do have younger people going to the site to help out their parents.

Industry/Entity Type

Healthcare

Coding

Coded - Design and coding required

Number of Pages Required

2 page

Colors

Designer to choose colors to be used in the design.

Requirements
Must have
• The code should be easily editable using textpad or VI. After the project is done I want to easily add my custom PHP code.
• The first page will be the home page and the other page I need is this form.
• https://www.stridewellfeet.com/stride-well-feet-do-i-qualify.php
Should not have
• I do not want to use Wordpress, Adobe Muse or another designing program.

```html
<!DOCTYPE html>
<html lang="en">
<head>
<meta charset="utf-8">
<title>Stride Well Feet – Diabetic Shoes</title>
<link rel="stylesheet" href="https://fonts.googleapis.com/css2?family=Open+Sans:wght@300;400;600;700;800&display=swap">
<style>
:root{
  --blue:#1b4f8b;
  --blue-dark:#143d6d;
  --green:#5cb85c;
  --text:#555;
  --heading:#333;
  --muted:#888;
  --line:#ddd;
  --light:#f2f2f2;
  --white:#fff;
}
*{box-sizing:border-box;margin:0;padding:0}
html,body{width:1200px;height:3232px;overflow:hidden;background:var(--white)}
body{font-family:"Open Sans",Arial,sans-serif;color:var(--text);position:relative}
.btn{position:absolute;background:var(--green);color:var(--white);font-weight:700;font-size:11px;border-radius:20px;text-align:center;text-transform:uppercase;letter-spacing:.3px;white-space:nowrap}

/* header */
.site-header{position:absolute;left:0;top:0;width:1200px;height:84px}
.brand{position:absolute;left:130px;top:22px;font-size:34px;font-weight:600;color:var(--blue);letter-spacing:-.5px;white-space:nowrap}
.brand small{font-size:24px;font-weight:600;color:var(--blue)}
.phone{position:absolute;left:820px;top:25px;display:flex;align-items:center;gap:10px;font-weight:700;font-size:15px;color:var(--heading);white-space:nowrap}
.phone .dot{width:32px;height:32px;border-radius:50%;background:var(--green);display:flex;align-items:center;justify-content:center}
.login{left:995px;top:24px;width:74px;height:34px;line-height:34px;font-size:12px}

/* nav */
.main-nav{position:absolute;left:0;top:84px;width:1200px;height:50px;background:var(--blue)}
.main-nav a{position:absolute;top:0;color:var(--white);font-size:11px;font-weight:600;text-transform:uppercase;text-decoration:none;line-height:50px;white-space:nowrap}
.main-nav a.active{left:134px;width:109px;text-align:center;background:var(--green)}

/* hero */
.hero{position:absolute;left:0;top:134px;width:1200px;height:496px;background:linear-gradient(100deg,#4a4034 0%,#8a6a43 35%,#c89a5a 55%,#6a5440 80%,#2e2a26 100%)}
.hero-title{position:absolute;left:642px;top:110px;width:426px;text-align:right;color:var(--white);font-size:50px;font-weight:300;white-space:nowrap}
.hero-title b{font-weight:800}
.hero-sub{position:absolute;left:642px;top:180px;width:426px;text-align:right;color:var(--white);font-size:21px;font-weight:700;white-space:nowrap}
.hero-text{position:absolute;left:642px;top:232px;width:426px;color:#f1f1f1;font-size:11.5px;line-height:21px;text-align:center}
.hero .btn{left:782px;top:323px;width:148px;height:38px;line-height:38px}
.arrow{position:absolute;top:222px;width:50px;height:50px;border-radius:50%;background:rgba(255,255,255,.75);display:flex;align-items:center;justify-content:center}

/* steps */
.section-title{position:absolute;left:0;width:1200px;text-align:center;color:var(--heading)}
.section-title .l1{font-size:23px;font-weight:300;display:block;letter-spacing:.5px}
.section-title .l2{font-size:23px;font-weight:800;display:block;letter-spacing:.5px}
.step{position:absolute;top:776px;width:212px;height:180px;border:1px solid var(--line);box-shadow:0 1px 4px rgba(0,0,0,.08);text-align:center}
.step .circle{width:96px;height:96px;border-radius:50%;background:var(--blue);margin:24px auto 0;display:flex;align-items:center;justify-content:center}
.step .label{color:var(--green);font-weight:700;font-size:12px;margin-top:18px}
.step-text{position:absolute;top:965px;width:212px;text-align:center;font-size:13px;line-height:22px;color:var(--text)}
.chev{position:absolute;top:852px}

/* video */
.video-band{position:absolute;left:0;top:1085px;width:1200px;height:412px;background:linear-gradient(90deg,#1e1c1a,#3a3530 55%,#2a2622)}
.video-band h2{position:absolute;left:130px;top:65px;color:var(--white);font-size:24px;font-weight:300}
.video-band h2 b{font-weight:800}
.video-band p{position:absolute;left:130px;width:430px;color:#ddd;font-size:11px;line-height:21px}
.video-band .btn{left:132px;top:300px;width:124px;height:40px;line-height:40px}
.player{position:absolute;left:628px;top:73px;width:448px;height:272px;background:var(--white);border:4px solid #ccc}
.player .frame{position:absolute;left:0;top:0;width:440px;height:240px;background:linear-gradient(180deg,#f7f7f7,#d6d6d6)}
.player .bar{position:absolute;left:0;top:240px;width:440px;height:24px;background:#e8e8e8;display:flex;align-items:center;gap:10px;padding:0 10px}
.player .track{flex:1;height:4px;background:#bbb}
.play{position:absolute;left:190px;top:94px;width:52px;height:52px;border-radius:50%;background:#333;display:flex;align-items:center;justify-content:center}

/* products */
.products-title{position:absolute;left:0;top:1546px;width:1200px;text-align:center;font-size:23px;color:var(--heading);font-weight:300}
.products-title b{font-weight:800}
.view-all{position:absolute;left:993px;top:1552px;width:74px;height:30px;border:1px solid var(--blue);color:var(--blue);font-size:10px;font-weight:700;text-align:center;line-height:28px}
.product{position:absolute;width:212px}
.product .photo{width:212px;height:170px;border:1px solid var(--line);background:var(--white);display:flex;align-items:center;justify-content:center}
.product .photo span{display:block;width:150px;height:70px;border-radius:40px 50px 12px 12px;background:linear-gradient(180deg,#8a8a8a,#444)}
.product .name{margin-top:12px;font-size:11px;line-height:18px;color:var(--blue);text-transform:uppercase}
.product .btn{position:relative;display:block;margin-top:10px;width:92px;height:34px;line-height:34px;font-size:10px}

/* about */
.about{position:absolute;left:0;top:2258px;width:1200px;height:194px;background:var(--blue)}
.about .pic{position:absolute;left:133px;top:30px;width:134px;height:134px;border-radius:50%;border:4px solid var(--white);background:linear-gradient(160deg,#b8cce0,#6d8aa6)}
.about .rule{position:absolute;left:295px;top:36px;width:2px;height:128px;background:#fff}
.about h2{position:absolute;left:322px;top:44px;color:var(--white);font-size:24px;font-weight:300}
.about h2 b{font-weight:800}
.about p{position:absolute;left:322px;top:88px;width:748px;color:#e6edf5;font-size:10.5px;line-height:21px}

/* catalog */
.catalog{position:absolute;left:0;top:2452px;width:1200px;height:453px;background:var(--light)}
.field{position:absolute;height:34px;background:var(--white);border:1px solid var(--line);font-size:10px;color:var(--muted);padding:10px 8px}
.field.select::after{content:"";position:absolute;right:10px;top:14px;border:4px solid transparent;border-top-color:#666}
.catalog .btn{left:928px;top:353px;width:140px;height:38px;line-height:38px}

/* footer columns */
.foot-col h3{position:absolute;font-size:13px;font-weight:700;color:var(--blue);text-transform:uppercase}
.foot-col p{position:absolute;font-size:10.5px;line-height:20px;color:var(--muted)}
.vline{position:absolute;top:2948px;width:1px;height:150px;background:var(--line)}
.maker{position:absolute;font-weight:700;color:var(--blue)}
.footer-bottom{position:absolute;left:0;top:3128px;width:1200px;height:104px;border-top:1px solid var(--line)}
.social{position:absolute;top:38px;width:26px;height:26px;border-radius:50%}
</style>
</head>
<body>

<header class="site-header">
  <div class="brand">stridewell <small>feet</small></div>
  <div class="phone"><span class="dot"><svg width="14" height="14" viewBox="0 0 24 24"><path fill="#fff" d="M6.6 10.8a15 15 0 0 0 6.6 6.6l2.2-2.2a1 1 0 0 1 1-.3 11 11 0 0 0 3.6.6 1 1 0 0 1 1 1V20a1 1 0 0 1-1 1A17 17 0 0 1 3 4a1 1 0 0 1 1-1h3.5a1 1 0 0 1 1 1c0 1.3.2 2.5.6 3.6a1 1 0 0 1-.3 1z"/></svg></span>1-800-555-0142</div>
  <div class="btn login">Log In</div>
</header>

<nav class="main-nav">
  <a class="active">Home</a>
  <a style="left:271px">Stride Well Feet! Do I Qualify!</a>
  <a style="left:491px">Why Diabetic Shoes?</a>
  <a style="left:670px">Shoes</a>
  <a style="left:769px">Products</a>
  <a style="left:892px">Shoe Fitter Jobs</a>
  <a style="left:1047px">FAQ</a>
</nav>

<section class="hero" role="img" aria-label="Photo of a runner's feet in sneakers on a road at sunset">
  <div class="arrow" style="left:56px"><svg width="12" height="12" viewBox="0 0 12 12"><path d="M8 1 3 6l5 5" stroke="#333" stroke-width="2" fill="none"/></svg></div>
  <div class="arrow" style="left:1092px"><svg width="12" height="12" viewBox="0 0 12 12"><path d="m4 1 5 5-5 5" stroke="#333" stroke-width="2" fill="none"/></svg></div>
  <h1 class="hero-title">DIABETIC <b>SHOES</b></h1>
  <div class="hero-sub">OR SNEAKERS COVERED BY VITACOR</div>
  <p class="hero-text">No or little out of pocket Cost To You!* Vitacor, and most insurance plans, may cover the cost of one pair of diabetic shoes and three pairs of custom inserts per calendar year. Co-payments...</p>
  <div class="btn">View More Info &#9656;</div>
</section>

<div class="section-title" style="top:680px"><span class="l1">4 EASY STEPS TO RECEIVE YOUR NEW</span><span class="l2">THERAPEUTIC SHOES</span></div>

<div class="step" style="left:131px"><div class="circle"><svg width="44" height="44" viewBox="0 0 44 44" fill="none" stroke="#fff" stroke-width="2.5"><rect x="8" y="6" width="24" height="32" rx="2"/><path d="M13 14h14M13 20h14M13 26h9M30 30l8-14"/></svg></div><div class="label">STEP 1</div></div>
<div class="step" style="left:373px"><div class="circle"><svg width="44" height="44" viewBox="0 0 44 44" fill="none" stroke="#fff" stroke-width="2.5"><rect x="9" y="5" width="26" height="34" rx="2"/><path d="M15 13h14M15 19h8"/><circle cx="25" cy="28" r="5"/><path d="m29 32 5 5"/></svg></div><div class="label">STEP 2</div></div>
<div class="step" style="left:615px"><div class="circle"><svg width="48" height="44" viewBox="0 0 48 44" fill="none" stroke="#fff" stroke-width="2.5"><path d="M4 30h40v6H4zM6 30l2-14h10l4 6 14 4a8 8 0 0 1 6 4"/></svg></div><div class="label">STEP 3</div></div>
<div class="step" style="left:857px"><div class="circle"><svg width="44" height="44" viewBox="0 0 44 44" fill="none" stroke="#fff" stroke-width="2.5"><rect x="6" y="20" width="8" height="18"/><path d="M14 22l7-14c3 0 4 2 3 6l-1 6h12a3 3 0 0 1 3 3l-3 13a3 3 0 0 1-3 2H14"/></svg></div><div class="label">STEP 4</div></div>
<svg class="chev" style="left:352px" width="14" height="20" viewBox="0 0 14 20"><path d="m3 3 7 7-7 7" stroke="#bbb" stroke-width="3" fill="none"/></svg>
<svg class="chev" style="left:594px" width="14" height="20" viewBox="0 0 14 20"><path d="m3 3 7 7-7 7" stroke="#bbb" stroke-width="3" fill="none"/></svg>
<svg class="chev" style="left:836px" width="14" height="20" viewBox="0 0 14 20"><path d="m3 3 7 7-7 7" stroke="#bbb" stroke-width="3" fill="none"/></svg>
<p class="step-text" style="left:131px">Fill out an application to<br>see if you qualify.</p>
<p class="step-text" style="left:373px">A prescription will befaxed<br>to your primary<br>physician.</p>
<p class="step-text" style="left:615px">After the prescription is signed,<br>a certified shoe fitter will fit<br>your new shoes.</p>
<p class="step-text" style="left:857px">Enjoy your new<br>shoes!</p>

<section class="video-band" role="img" aria-label="Dark background photo of a person tying running shoes">
  <h2>OUR <b>VIDEO</b></h2>
  <p style="top:118px">Sed ut perspiciatis unde omnis iste natus error sit voluptatem accusantium doloremque laudantium, totam rem aperiam, eaque ipsa quae ab illo inventore veritatis et quasi architecto beatae vitae dicta sunt explicabo. Nemo enim ipsam voluptatem quia voluptas sit aspernatur aut odit aut fugit, sed quia consequuntur</p>
  <p style="top:214px">Sed ut perspiciatis unde omnis iste natus error sit voluptatem accusantium doloremque laudantium, totam rem aperiam, eaque ipsa quae ab illo inventore veritatis et quasi architecto beatae vitae dicta sunt explicabo.</p>
  <div class="btn">More Videos &#9656;</div>
  <div class="player">
    <div class="frame" role="img" aria-label="Video still promoting the supplier with a sign-up message and a row of diabetic shoes"></div>
    <div class="play"><svg width="18" height="20" viewBox="0 0 18 20"><path d="M3 2v16l13-8z" fill="#fff"/></svg></div>
    <div class="bar"><svg width="10" height="12" viewBox="0 0 10 12"><path d="M1 1v10l8-5z" fill="#444"/></svg><span style="font-size:8px;color:#555">00:00:00</span><span class="track"></span><svg width="12" height="12" viewBox="0 0 12 12"><path d="M1 4h3l4-3v10L4 8H1z" fill="#444"/></svg><span style="width:50px;height:4px;background:#c33"></span></div>
  </div>
</section>

<h2 class="products-title">FEATURE <b>PRODUCTS</b></h2>
<div class="view-all">VIEW ALL</div>

<div class="product" style="left:131px;top:1612px"><div class="photo" role="img" aria-label="Black trail walking shoe"><span></span></div><div class="name">Solvera - R101:Slate Path<br>Walker-Lace</div><div class="btn">Add To Cart</div></div>
<div class="product" style="left:373px;top:1612px"><div class="photo" role="img" aria-label="Navy and lime sport running shoe"><span style="background:linear-gradient(180deg,#4a6a9a,#2a3d5a)"></span></div><div class="name">Solvera - R205:Navy/Lime<br>Sport Runner-Lace</div><div class="btn">Add To Cart</div></div>
<div class="product" style="left:615px;top:1612px"><div class="photo" role="img" aria-label="Grey and black sport running shoe"><span style="background:linear-gradient(180deg,#b0b0b0,#777)"></span></div><div class="name">Solvera - R205:Ash/Black<br>Sport Runner-Lace</div><div class="btn">Add To Cart</div></div>
<div class="product" style="left:857px;top:1612px"><div class="photo" role="img" aria-label="Black casual dress shoe"><span style="background:linear-gradient(180deg,#444,#111)"></span></div><div class="name">Solvera - R310:Onyx Casual<br>Dress-Lace</div><div class="btn">Add To Cart</div></div>

<div class="product" style="left:131px;top:1932px"><div class="photo" role="img" aria-label="Brown casual dress shoe"><span style="background:linear-gradient(180deg,#a0603a,#5a2e16)"></span></div><div class="name">Solvera - R310:Chestnut<br>Casual Dress-Lace</div><div class="btn">Add To Cart</div></div>
<div class="product" style="left:373px;top:1932px"><div class="photo" role="img" aria-label="Black sport walker shoe with hook straps"><span style="background:linear-gradient(180deg,#666,#222)"></span></div><div class="name">Solvera - R418:Onyx Sport<br>Walker-Strap</div><div class="btn">Add To Cart</div></div>
<div class="product" style="left:615px;top:1932px"><div class="photo" role="img" aria-label="White sport walker shoe with hook straps"><span style="background:linear-gradient(180deg,#f2f2f2,#c4c4c4)"></span></div><div class="name">Solvera - R418:Ivory Sport<br>Walker-Strap</div><div class="btn">Add To Cart</div></div>
<div class="product" style="left:857px;top:1932px"><div class="photo" role="img" aria-label="Grey trail walking shoe with green accents"><span style="background:linear-gradient(180deg,#6a6e5a,#2e3028)"></span></div><div class="name">Solvera - R522:Graphite<br>Trail Walker-Lace</div><div class="btn">Add To Cart</div></div>

<section class="about">
  <div class="pic" role="img" aria-label="Photo of the company office building"></div>
  <div class="rule"></div>
  <h2>ABOUT <b>US</b></h2>
  <p>Stride Well Feet was created by Keystone Medical Supply to educate clients and prospective shoe fitters about diabetic shoes and the coverage that Vitacor provides. Founded by a Board-Certified Pedorthist, the company's mission is to help clients receive properly fitted shoes from qualified healthcare professionals around the United States. Keystone Medical Supply works directly with Vitacor to determine the patient's coverage.</p>
</section>

<section class="catalog">
  <div class="section-title" style="top:50px"><span class="l1">REQUEST A FREE DIABETIC</span><span class="l2">SHOE CATALOG</span></div>
  <div class="field" style="left:131px;top:150px;width:226px">First Name:</div>
  <div class="field" style="left:365px;top:150px;width:225px">Last Name:</div>
  <div class="field" style="left:131px;top:194px;width:226px">Address:</div>
  <div class="field" style="left:365px;top:194px;width:225px">City:</div>
  <div class="field" style="left:131px;top:238px;width:226px">State:</div>
  <div class="field" style="left:365px;top:238px;width:225px">Zip:</div>
  <div class="field" style="left:131px;top:282px;width:226px">Phone:</div>
  <div class="field" style="left:365px;top:282px;width:225px">Best time to Call:</div>
  <div class="field" style="left:131px;top:326px;width:226px">Email:</div>
  <div class="field select" style="left:365px;top:326px;width:225px">Primary Insurance:</div>
  <div class="field select" style="left:612px;top:150px;width:456px">Do you want to check eligibility Online?</div>
  <div class="field" style="left:612px;top:194px;width:456px;height:166px">Comments:</div>
  <div class="btn">Request Catalog</div>
</section>

<div class="foot-col">
  <h3 style="left:131px;top:2950px">Our Philosophy</h3>
  <p style="left:131px;top:2984px;width:280px">At Keystone Medical Supply, we understand the health benefits and medical safety associated with properly fitted shoes. We strive to educate clients about wearing appropriate footwear and avoiding...</p>
  <p style="left:131px;top:3072px;color:var(--green);font-weight:700;font-size:10px">LEARN MORE INFO &#9656;</p>
  <div class="vline" style="left:430px"></div>
  <h3 style="left:455px;top:2950px">Our Manufacturers</h3>
  <div class="maker" style="left:455px;top:3010px;font-size:22px">Amblewell</div>
  <div class="maker" style="left:598px;top:3012px;font-size:20px;color:var(--heading)">Pedilux</div>
  <div class="vline" style="left:770px"></div>
  <h3 style="left:795px;top:2950px">FAQ</h3>
  <svg style="position:absolute;left:1022px;top:2952px" width="32" height="12" viewBox="0 0 32 12"><circle cx="6" cy="6" r="4.5" fill="none" stroke="#aaa"/><circle cx="22" cy="6" r="4.5" fill="none" stroke="#555"/></svg>
  <p style="left:795px;top:2980px;color:var(--blue);font-weight:600;font-size:10.5px">HOW DOES DIABETES CAUSE FOOT PROBLEMS?</p>
  <p style="left:795px;top:3004px;width:275px;font-size:10px">Diabetes can cause neuropathy (nerve damage), which reduces feeling in your feet. This makes you less likely to feel the early warning signs of <span style="color:var(--green)">...MORE</span></p>
</div>

<footer class="footer-bottom">
  <div class="brand" style="left:130px;top:22px;font-size:26px">stridewell <small style="font-size:19px">feet</small></div>
  <p style="position:absolute;left:131px;top:64px;font-size:9px;color:var(--muted)">COPYRIGHTS © STRIDEWELLFEET, 2017 | ALL RIGHTS RESERVED.</p>
  <span class="social" style="left:943px;background:#3b5998"></span>
  <span class="social" style="left:973px;background:#1da1f2"></span>
  <span class="social" style="left:1003px;background:#cc2b2b"></span>
  <span class="social" style="left:1033px;background:#b5773f"></span>
  <p style="position:absolute;left:1115px;top:44px;font-size:10px;color:var(--muted)">CT1</p>
</footer>

</body>
</html>
```